Clockharbor Homepage Banner 1060 W x 100 H

Please see the attached 'word' document (Also copied below)
Feel free to use any images or logos from our website.
www.clockharbor.com.au

Background:
We are an Australian based official watch distributor/online retailer of international watch brands.

We require a new banner ad (1060 W x 100 H) to replace the existing one on our homepage www.clockharbor.com.au & wish to convey the following information:
*(Please feel free to alter wording, include or exclude points below & generally take creative license (with commercial reality in mind). We sell some luxury watches, so it must look professional & maintain a luxury look & feel.)

Clockharbor Direct:
Revolutionising the retail watch market !

- Buy direct from the official distributor & get world competitive
online prices (with full international warranty, & all original
papers, box & invoice)

- Eliminate all risk of fakes & non-existent factory warranty from
'grey' market sellers

- Free worldwide delivery over A$300

- Order online & 'try-on' in the comfort of your own home.
If you're not 100% happy, just post it back for a full refund or
exchange within 30 days

- Prefer to see & try on before purchase? Visit one of our retail
partner stores.

*** Feel free to copy any images from our website
www.clockharbor.com.au
Updates

Target Market(s)

Luxury watches

Industry/Entity Type

Retail

Font styles to use
Sans Serif

Requirements
Must have
• Visual imagery, text
Nice to have
• Feel free to use your creativity...
Should not have
• Cheap looking or tacky images. We sell some luxury watches, so we need to keep a professional & luxury image.

```html
<!DOCTYPE html>
<html lang="en">
<head>
<meta charset="utf-8">
<title>Clockharbor Homepage Banner</title>
<link rel="stylesheet" href="https://fonts.googleapis.com/css2?family=Arimo:wght@400;700&display=swap">
<style>
  :root {
    --stage: #8c583a;
    --banner: #ffffff;
    --navy-band: #08086a;
    --headline: #0d2c6b;
    --note-grey: #9c9c9c;
    --brand-blue: #1b3a78;
    --watch-steel: #9fb2c8;
    --watch-strap: #3e5f95;
    --button-top: #8a8a8a;
    --button-bottom: #3a3a3a;
    --white: #ffffff;
  }
  html, body {
    margin: 0;
    padding: 0;
    width: 1200px;
    height: 324px;
    overflow: hidden;
    background: var(--stage);
  }
  .canvas {
    position: relative;
    width: 1200px;
    height: 324px;
    font-family: "Arimo", Arial, sans-serif;
  }
  .banner {
    position: absolute;
    left: 47px;
    top: 109px;
    width: 1107px;
    height: 104px;
    background: var(--banner);
    box-shadow: 0 2px 6px rgba(0,0,0,0.35);
  }
  .headline {
    position: absolute;
    left: 33px;
    top: 4px;
    margin: 0;
    font-size: 51px;
    font-weight: 700;
    letter-spacing: -0.5px;
    color: var(--headline);
    transform: scaleY(1.08);
    transform-origin: top left;
  }
  .offer-band {
    position: absolute;
    left: 8px;
    top: 71px;
    width: 529px;
    height: 24px;
    background: var(--navy-band);
  }
  .offer-band p {
    margin: 0;
    padding-left: 28px;
    line-height: 25px;
    font-size: 14px;
    font-weight: 700;
    color: var(--white);
  }
  .watch-visual {
    position: absolute;
    left: 510px;
    top: 5px;
    width: 61px;
    height: 93px;
    border-radius: 30px 30px 8px 8px;
    background: linear-gradient(180deg, var(--watch-steel) 0%, var(--watch-steel) 55%, var(--watch-strap) 100%);
  }
  .warranty-note {
    position: absolute;
    left: 596px;
    top: 30px;
    margin: 0;
    font-size: 16px;
    line-height: 19px;
    font-weight: 700;
    color: var(--note-grey);
  }
  .brand {
    position: absolute;
    left: 904px;
    top: 9px;
    display: flex;
    align-items: center;
    gap: 6px;
  }
  .brand-dot {
    width: 31px;
    height: 31px;
    border-radius: 50%;
    background: var(--brand-blue);
  }
  .brand-name {
    font-size: 22px;
    font-weight: 700;
    color: var(--brand-blue);
  }
  .cta-panel {
    position: absolute;
    left: 824px;
    top: 49px;
    width: 275px;
    height: 46px;
  }
  .visit-button {
    position: absolute;
    left: 87px;
    top: 10px;
    width: 101px;
    height: 24px;
    border-radius: 5px;
    background: linear-gradient(180deg, var(--button-top), var(--button-bottom));
    color: var(--white);
    font-size: 12.5px;
    line-height: 24px;
    text-align: center;
    box-shadow: 0 1px 2px rgba(0,0,0,0.4);
  }
</style>
</head>
<body>
<div class="canvas">
  <section class="banner">
    <h1 class="headline">Buy direct</h1>
    <div class="offer-band">
      <p>from the official distributor &amp; get world competitive</p>
    </div>
    <div class="watch-visual" role="img" aria-label="Luxury chronograph watch with steel case and blue strap"></div>
    <p class="warranty-note">(with full international<br>warranty, &amp; all original<br>papers, box &amp; invoice)</p>
    <div class="brand">
      <span class="brand-dot"></span>
      <span class="brand-name">Clockharbor</span>
    </div>
    <div class="cta-panel">
      <svg width="275" height="46" viewBox="0 0 275 46" aria-hidden="true">
        <polygon points="0,46 45,0 275,0 275,46" fill="var(--navy-band)"/>
      </svg>
      <div class="visit-button">Visit More</div>
    </div>
  </section>
</div>
</body>
</html>
```